ALL TEXT GRAPHICS TM May 2025 for Instagram

We are looking for a series of social media graphics for Instagram (new size: 4:5 (1080 x 1350 pixels) ratio that are ALL TEXT. We want the following quotes below on each graphic; one quote per graphic. AND, In very small letters at the bottom of each graphic, add @TovaMarshOnline
The look and feel of these graphics should be complimentary to the color palette attached below; but keep them simple. But the design is up to you; at the end of this document, I provided various samples of all text graphics that I like as examples.
Target Market(s)
women looking to lose weight
Look and feel

```html
<!DOCTYPE html>
<html lang="en">
<head>
<meta charset="utf-8">
<title>All Text Graphics — Tova Marsh</title>
<link rel="stylesheet" href="https://fonts.googleapis.com/css2?family=Poppins:wght@400;500;600;700&family=Questrial&family=Playfair+Display:wght@500;600;700;800;900&family=Rokkitt:wght@700&display=swap">
<style>
  :root {
    --page: #ffffff;
    --card: #ffffff;
    --hot-pink: #ff0a80;
    --soft-pink: #ff9dcd;
    --bright-pink: #ff4fa8;
    --candy-pink: #ff62b5;
    --magenta: #d1006a;
    --ink: #3b3b3b;
    --ink-black: #1e1e1e;
    --handle: #777777;
  }
  * { margin: 0; padding: 0; box-sizing: border-box; }
  html, body { width: 1200px; height: 1200px; overflow: hidden; background: var(--page); }
  .sheet { position: relative; width: 1200px; height: 1200px; }
  .post {
    position: absolute; width: 419px; height: 523px; overflow: hidden;
    background: var(--card);
    box-shadow: 0 2px 14px rgba(0,0,0,0.07);
  }
  .post--one { left: 169px; top: 60px; }
  .post--two { left: 620px; top: 60px; }
  .post--three { left: 169px; top: 625px; }
  .post--four { left: 620px; top: 625px; }
  .line { position: absolute; white-space: nowrap; line-height: 1; }
  .center { left: 0; right: 0; text-align: center; }
  .sans-heavy { font-family: "Poppins", sans-serif; font-weight: 700; }
  .body-copy { font-family: "Questrial", sans-serif; color: var(--ink); letter-spacing: 1px; }
  .serif-head { font-family: "Playfair Display", serif; }
  .slab { font-family: "Rokkitt", serif; font-weight: 700; transform-origin: left top; }
  .handle {
    position: absolute; left: 0; right: 0; top: 486px; text-align: center; line-height: 1;
    font-family: "Playfair Display", serif; font-size: 13px; letter-spacing: 0.8px;
    color: var(--handle); text-transform: uppercase;
  }
</style>
</head>
<body>
<main class="sheet">

  <section class="post post--one">
    <p class="line center sans-heavy" style="top:39px;font-size:65px;color:var(--hot-pink);letter-spacing:-1px;">TIRED</p>
    <p class="line center sans-heavy" style="top:95px;font-size:58px;color:var(--soft-pink);letter-spacing:-1px;">MOODY</p>
    <p class="line center sans-heavy" style="top:147px;font-size:34px;color:var(--magenta);letter-spacing:-0.3px;">STUBBORN BELLY FAT</p>
    <p class="line center body-copy" style="top:251px;font-size:37px;line-height:40px;">Your hormones are<br>screaming for help!</p>
    <p class="line center serif-head" style="top:402px;font-size:37px;font-weight:800;color:var(--magenta);letter-spacing:1.5px;">LET’S FIX THAT</p>
    <p class="handle">@TovaMarshOnline</p>
  </section>

  <section class="post post--two">
    <p class="line serif-head" style="left:28px;top:41px;font-size:28px;font-weight:600;color:var(--ink);">THAT STUBBORN WEIGHT?</p>
    <p class="line sans-heavy" style="left:30px;top:71px;font-size:54px;color:var(--hot-pink);letter-spacing:-1px;">IT’S NOT</p>
    <p class="line sans-heavy" style="left:33px;top:120px;font-size:35px;color:var(--bright-pink);letter-spacing:-0.5px;">YOUR FAULT.</p>
    <p class="line body-copy" style="left:32px;top:209px;font-size:36px;line-height:31px;">Your hormones<br>are to blame and<br>you’re not alone</p>
    <p class="line slab" style="left:33px;top:371px;font-size:45px;color:var(--bright-pink);letter-spacing:2px;transform:scaleX(0.7);">BUT THERE IS A FIX.</p>
    <p class="handle">@TovaMarshOnline</p>
  </section>

  <section class="post post--three">
    <p class="line slab" style="left:29px;top:56px;font-size:41px;color:var(--ink);transform:scaleX(0.69);">YOUR BELLY ISN’T FAT…</p>
    <p class="line sans-heavy" style="left:30px;top:90px;font-size:44px;color:var(--candy-pink);letter-spacing:-0.5px;">IT’S HORMONAL.</p>
    <p class="line slab" style="left:33px;top:182px;font-size:55px;line-height:44px;color:var(--magenta);transform:scaleX(0.7);">AND HERE’S<br>HOW TO FIX IT.</p>
    <p class="line" style="left:30px;top:307px;font-family:'Poppins',sans-serif;font-size:32px;color:var(--ink-black);">COMMENT</p>
    <p class="line" style="left:31px;top:335px;font-family:'Poppins',sans-serif;font-weight:600;font-size:48px;color:var(--candy-pink);">HORMONES</p>
    <p class="line body-copy" style="left:31px;top:383px;font-size:35px;letter-spacing:1.5px;">if nothing is working.</p>
    <p class="handle">@TovaMarshOnline</p>
  </section>

  <section class="post post--four">
    <p class="line slab" style="left:27px;top:54px;font-size:43px;color:var(--magenta);transform:scaleX(0.66);">THE STUBBORN BELLY FAT</p>
    <p class="line slab" style="left:27px;top:91px;font-size:55px;color:var(--magenta);transform:scaleX(0.77);">AFTER 40?</p>
    <p class="line" style="left:30px;top:182px;font-family:'Poppins',sans-serif;font-weight:500;font-size:32px;color:var(--ink);">It’s not about calories;</p>
    <p class="line sans-heavy" style="left:30px;top:217px;font-size:41px;line-height:38px;color:var(--candy-pink);">it’s about<br>your hormones.</p>
    <p class="line serif-head" style="left:28px;top:347px;font-size:44px;font-weight:900;color:var(--magenta);letter-spacing:-3.5px;">HERE IS THE FIX!</p>
    <p class="handle">@TovaMarshOnline</p>
  </section>

</main>
</body>
</html>
```